Letterhead Design for Law Firm that Specializes in Property Damage Litigation

We are looking for a redesign of our letterhead. Our current letterhead lists all of our current staff members and we'd like to come up with a design that does NOT list all of the staff members so that it does not need to be updated with every newly hired employee. Must be in editable format.

We are a law firm that specializes in property damage, so we need something that is professional, yet modern. The final design should use our existing logo and should use a blue color scheme (alternate colors would be gray, black, and white).

Industry/Entity Type

Legal

Colors
0054AA
0677BA
7BADD7
CADEEF
E8F1F8

```html
<!DOCTYPE html>
<html lang="en">
<head>
<meta charset="UTF-8">
<title>Hartwell Crane &amp; Ostrander — Letterhead</title>
<link href="https://fonts.googleapis.com/css2?family=Montserrat:wght@400;500;600;700&display=swap" rel="stylesheet">
<style>
  :root {
    --navy: #0054AA;
    --blue: #0677BA;
    --sky: #7BADD7;
    --mist: #CADEEF;
    --ice: #E8F1F8;
    --ink: #3a3f47;
    --grey: #6d737b;
    --rule: #b9bec5;
    --paper: #ffffff;
    --backdrop: #eceef0;
  }
  * { box-sizing: border-box; margin: 0; padding: 0; }
  html, body {
    width: 1200px; height: 900px; overflow: hidden;
    background: var(--backdrop);
    font-family: "Montserrat", Arial, sans-serif;
    color: var(--ink);
  }
  .letterhead {
    position: absolute; left: 300px; top: 26px;
    width: 600px; height: 848px; overflow: hidden;
    background: var(--paper);
    box-shadow: 0 6px 24px rgba(0,0,0,0.10);
  }
  .background-wash {
    position: absolute; left: 250px; top: 250px;
    width: 350px; height: 520px;
    background: linear-gradient(200deg, rgba(202,222,239,0.55), rgba(232,241,248,0.15) 70%, rgba(255,255,255,0));
  }
  .brand {
    position: absolute; left: 58px; top: 62px;
  }
  .brand-name {
    display: flex; align-items: flex-start; gap: 10px;
  }
  .brand-mark {
    width: 14px; height: 14px; margin-top: 3px;
    background: var(--navy); flex: none;
  }
  .brand-lines {
    font-weight: 600; font-size: 16px; line-height: 1.1;
    color: var(--navy); letter-spacing: 0.06em; text-transform: uppercase;
  }
  .brand-lines span { display: block; }
  .brand-tagline {
    margin-top: 9px;
    font-size: 7px; letter-spacing: 0.26em; text-transform: uppercase;
    color: var(--grey);
  }
  .offices {
    position: absolute; top: 62px; right: 62px;
    display: flex; gap: 22px;
  }
  .office {
    border-left: 1px solid var(--rule);
    padding-left: 9px;
    font-size: 6.5px; line-height: 1.55; color: var(--grey);
  }
  .office-title { font-weight: 700; color: var(--navy); margin-bottom: 2px; }
  .office-line { display: flex; align-items: center; gap: 4px; }
  .office-line.indent { padding-left: 11px; }
  .office-line svg { width: 7px; height: 7px; fill: var(--navy); flex: none; }
  .letter-body {
    position: absolute; left: 62px; top: 232px; width: 400px;
    font-size: 8.6px; line-height: 1.5; color: var(--ink);
  }
  .letter-body p + p { margin-top: 12px; }
  .signature {
    position: absolute; left: 200px; top: 520px;
  }
  .signature-mark {
    width: 110px; height: 30px;
    background: linear-gradient(90deg, var(--ice), var(--mist));
    border-radius: 4px;
  }
  .signature-role { font-size: 8.6px; color: var(--ink); margin-top: 3px; }
  .website {
    position: absolute; left: 62px; bottom: 42px;
    font-size: 7.5px; font-weight: 700; color: var(--navy);
  }
</style>
</head>
<body>
  <main class="letterhead">
    <div class="background-wash" role="img" aria-label="Faint pale-blue background decoration"></div>

    <header class="brand">
      <div class="brand-name">
        <span class="brand-mark"></span>
        <div class="brand-lines">
          <span>Hartwell</span>
          <span>Crane &amp;</span>
          <span>Ostrander</span>
        </div>
      </div>
      <div class="brand-tagline">The Property Damage Attorneys</div>
    </header>

    <section class="offices">
      <div class="office">
        <div class="office-title">Philadelphia Office</div>
        <div class="office-line"><svg viewBox="0 0 10 10"><path d="M2 0.5 L4 2.5 L3 4 Q4.5 6 6 7 L7.5 6 L9.5 8 L8 9.5 Q3.5 9 0.5 2 Z"/></svg>215.555.0140</div>
        <div class="office-line"><svg viewBox="0 0 10 10"><path d="M2 0.5 L4 2.5 L3 4 Q4.5 6 6 7 L7.5 6 L9.5 8 L8 9.5 Q3.5 9 0.5 2 Z"/></svg>215.555.0141</div>
        <div class="office-line"><svg viewBox="0 0 10 10"><path d="M5 0.5 A3.3 3.3 0 0 1 8.3 3.8 C8.3 6 5 9.5 5 9.5 C5 9.5 1.7 6 1.7 3.8 A3.3 3.3 0 0 1 5 0.5 Z M5 2.6 A1.2 1.2 0 1 0 5 5 A1.2 1.2 0 1 0 5 2.6 Z"/></svg>1617 Market Street</div>
        <div class="office-line indent">Suite 1200</div>
        <div class="office-line indent">Philadelphia, PA 19103</div>
      </div>
      <div class="office">
        <div class="office-title">New Jersey Office</div>
        <div class="office-line"><svg viewBox="0 0 10 10"><path d="M2 0.5 L4 2.5 L3 4 Q4.5 6 6 7 L7.5 6 L9.5 8 L8 9.5 Q3.5 9 0.5 2 Z"/></svg>856.555.0170</div>
        <div class="office-line"><svg viewBox="0 0 10 10"><path d="M2 0.5 L4 2.5 L3 4 Q4.5 6 6 7 L7.5 6 L9.5 8 L8 9.5 Q3.5 9 0.5 2 Z"/></svg>856.555.0171</div>
        <div class="office-line"><svg viewBox="0 0 10 10"><path d="M5 0.5 A3.3 3.3 0 0 1 8.3 3.8 C8.3 6 5 9.5 5 9.5 C5 9.5 1.7 6 1.7 3.8 A3.3 3.3 0 0 1 5 0.5 Z M5 2.6 A1.2 1.2 0 1 0 5 5 A1.2 1.2 0 1 0 5 2.6 Z"/></svg>2200 Route 70 West</div>
        <div class="office-line indent">Suite 305</div>
        <div class="office-line indent">Cherry Hill, NJ 08002</div>
      </div>
    </section>

    <article class="letter-body">
      <p>Letterhead samples are a great way of deciding what kind of letterhead you want to design for you and your company. The internet has a ton of great letterhead samples to browse through. Whether you want something simple, with just a couple lines of text of your business information, or something decorative and stunning, with photos and logos on the top and bottom of the page, it will be easy to find what you want, because there are samples online for basically any type of letterhead you could want.</p>
      <p>Any business could easily benefit from browsing through some letterhead samples, if only to get an idea for what kind of letterhead their company might want. Letterheads are just one of the tools that a business professional could use to help increase their customer base, and to really be memorable to everyone they write a letter to. Letterhead is quite an effective tool for marketing and advertising, but because it's such a simple and well known idea, it is often unfairly overlooked. Make sure you don't make that mistake, and make some letterhead samples of your own today.</p>
      <p>Whether you want to get new customers to remember you and become part of your clientele, or you just want to send out friendly reminders to your existing clients, customizing your own letterhead samples can really help you out. Try out some letterhead samples and you will not regret it, and I'm sure you will add a new tool to your business' arsenal of networking, marketing, and advertising tools.</p>
    </article>

    <div class="signature">
      <div class="signature-mark" role="img" aria-label="Handwritten signature of Daniel Whitford"></div>
      <div class="signature-role">company director</div>
    </div>

    <footer class="website">www.hcolegal.com</footer>
  </main>
</body>
</html>
```